we need a business card in yellow, green and black with rounded edges. We are in the Construction and Engineering business. I need the below info included:

Neil Barton
Bluestone Engineering & Construction, Inc.
4168 Harbor Crest Road,
Santa Ana, Ca 92814
714-555-0147 Office
714-555-0192 Cell
714-555-0163 Fax
nb@bluestonexq.example

thanks for your help!

```html
<!DOCTYPE html>
<html lang="en">
<head>
<meta charset="utf-8">
<title>Bluestone Engineering &amp; Construction – Business Card</title>
<link rel="stylesheet" href="https://fonts.googleapis.com/css2?family=Quicksand:wght@500;700&display=swap">
<style>
  :root {
    --page-bg: #dcdcdc;
    --card-black: #1e1e1e;
    --card-black-deep: #161616;
    --brand-green: #1fb440;
    --brand-green-dark: #128a2c;
    --brand-yellow: #d8cc12;
    --text-light: #e6e6e6;
    --text-muted: #c4c4c4;
  }
  * { box-sizing: border-box; margin: 0; padding: 0; }
  html, body {
    width: 1200px; height: 750px; overflow: hidden;
    background: var(--page-bg);
    font-family: "Quicksand", "Trebuchet MS", sans-serif;
  }
  .card {
    position: absolute; left: 162px; top: 125px;
    width: 876px; height: 500px;
    border-radius: 42px; overflow: hidden;
    background: radial-gradient(ellipse at 35% 40%, var(--card-black) 0%, var(--card-black-deep) 100%);
  }
  .card__sweep { position: absolute; inset: 0; width: 100%; height: 100%; }
  .brand-mark {
    position: absolute; left: 560px; top: 52px;
    display: flex; align-items: center; gap: 14px;
    color: var(--brand-green); font-weight: 700; font-size: 30px;
  }
  .brand-mark__square { width: 44px; height: 44px; background: var(--brand-green); }
  .company { position: absolute; left: 56px; top: 170px; }
  .company__name { color: var(--brand-yellow); font-weight: 700; font-size: 46px; line-height: 1; }
  .company__legal { color: var(--text-light); font-weight: 500; font-size: 27px; margin-top: 4px; }
  .company__address {
    position: absolute; left: 56px; top: 268px;
    color: var(--text-muted); font-weight: 500; font-size: 20px;
  }
  .contact { position: absolute; left: 56px; top: 330px; }
  .contact__name { color: var(--brand-yellow); font-weight: 700; font-size: 30px; line-height: 1.1; margin-bottom: 6px; }
  .contact__list { list-style: none; }
  .contact__item {
    display: flex; align-items: center; gap: 10px;
    color: var(--text-light); font-weight: 500; font-size: 19px; line-height: 25px;
  }
  .contact__icon { width: 18px; height: 18px; fill: var(--brand-green); flex: none; }
</style>
</head>
<body>
  <article class="card">
    <svg class="card__sweep" viewBox="0 0 876 500" aria-hidden="true">
      <path d="M742 0 C860 130 840 380 560 500 L876 500 L876 0 Z" fill="var(--brand-green)"/>
      <path d="M742 0 C860 130 840 380 560 500" fill="none" stroke="var(--brand-green-dark)" stroke-width="4"/>
    </svg>

    <div class="brand-mark">
      <span class="brand-mark__square"></span>
      <span class="brand-mark__name">Bluestone</span>
    </div>

    <header class="company">
      <h1 class="company__name">Bluestone</h1>
      <p class="company__legal">Engineering &amp; Construction, Inc.</p>
    </header>
    <p class="company__address">4168 Harbor Crest Road, Santa Ana, Ca 92814</p>

    <section class="contact">
      <h2 class="contact__name">Neil Barton</h2>
      <ul class="contact__list">
        <li class="contact__item">
          <svg class="contact__icon" viewBox="0 0 20 20"><path d="M10 2 1 10h3v8h5v-5h2v5h5v-8h3z"/></svg>
          4168 Harbor Crest Road
        </li>
        <li class="contact__item">
          <svg class="contact__icon" viewBox="0 0 20 20"><path d="M5 2h3l1.5 4-2 1.5a10 10 0 0 0 5 5l1.5-2 4 1.5v3c0 1-1 2-2 2C9 17 3 11 3 4c0-1 1-2 2-2z"/></svg>
          714-555-0147
        </li>
        <li class="contact__item">
          <svg class="contact__icon" viewBox="0 0 20 20"><path d="M6 1h8a1 1 0 0 1 1 1v16a1 1 0 0 1-1 1H6a1 1 0 0 1-1-1V2a1 1 0 0 1 1-1zm1 2v12h6V3z"/></svg>
          714-555-0192
        </li>
        <li class="contact__item">
          <svg class="contact__icon" viewBox="0 0 20 20"><path d="M5 2h8v5H5zM2 8h16v8h-3v2H5v-2H2zm5 6v3h6v-3z"/></svg>
          714-555-0163
        </li>
        <li class="contact__item">
          <svg class="contact__icon" viewBox="0 0 20 20"><path d="M2 4h16v12H2zm2 2v.5l6 4 6-4V6l-6 4z"/></svg>
          nb@bluestonexq.example
        </li>
      </ul>
    </section>
  </article>
</body>
</html>
```